Updated Business Card Re-design (Logo Provided)

I am needing to update our business cards for our practice, Bright Care Partners. We are a personal injury and wellness practice. The final design should be elegant and classy, but a type of card people would want to keep. Any samples should only have Dr. Tomas Verlinde on the template.
Updates

Went on vacation/holiday

Need extra days to review

Target Market(s)

Personal Injury clients, wellness clients

Industry/Entity Type

Personal Injury, medical, wellness

Contact Information for Business Card

dr and practice name, offerings

Requirements
Must have
• Single sided, this will be printed on a transparent business card, no exceptions.

```html
<!DOCTYPE html>
<html lang="en">
<head>
<meta charset="utf-8">
<title>Bright Care Partners – Business Card</title>
<link rel="stylesheet" href="https://fonts.googleapis.com/css2?family=Montserrat:wght@400;500;700;800&display=swap">
<style>
  :root {
    --page: #e0e0e0;
    --card: #fafafa;
    --orange: #f7931e;
    --blue: #0674bb;
    --green: #2e8b4e;
    --ink: #1d1d1f;
    --white: #ffffff;
  }
  * { margin: 0; padding: 0; box-sizing: border-box; }
  html, body { width: 825px; height: 1200px; overflow: hidden; }
  body { background: var(--page); font-family: "Montserrat", sans-serif; position: relative; }

  .card { position: absolute; left: 30px; top: 380px; width: 765px; height: 440px; background: var(--card); overflow: hidden; }

  .brand-mark { position: absolute; left: 62px; top: 44px; display: flex; align-items: center; gap: 8px; }
  .brand-mark .dot { width: 22px; height: 22px; border-radius: 50%; background: var(--orange); }
  .brand-mark .word { font-weight: 700; font-size: 22px; color: var(--green); line-height: 1; }

  .practice { position: absolute; left: 240px; top: 42px; }
  .practice-name { font-weight: 800; font-size: 26px; color: var(--orange); letter-spacing: 0.2px; line-height: 1; text-transform: uppercase; }
  .practice-tagline { font-weight: 500; font-size: 21px; color: var(--green); margin-top: 6px; line-height: 1; }

  .services { position: absolute; left: 0; top: 123px; width: 765px; height: 94px; background: var(--blue); }
  .service { position: absolute; display: flex; align-items: center; gap: 14px; color: var(--white); font-size: 18px; font-weight: 500; white-space: nowrap; }
  .service svg { width: 21px; height: 21px; flex: none; }

  .doctor-tab { position: absolute; left: 0; top: 217px; width: 765px; height: 57px; }
  .doctor { position: absolute; left: 237px; top: 225px; display: flex; align-items: center; gap: 16px; color: var(--white); }
  .doctor svg { width: 26px; height: 26px; }
  .doctor-name { font-weight: 700; font-size: 21px; line-height: 1; }
  .doctor-assoc { font-weight: 500; font-size: 11.5px; margin-top: 4px; line-height: 1; }

  .contact { position: absolute; top: 289px; width: 200px; text-align: center; color: var(--ink); font-size: 16.5px; font-weight: 500; line-height: 23px; }
  .contact svg { display: block; margin: 0 auto 14px; width: 38px; height: 38px; }
  .contact.phone { left: -15px; }
  .contact.email { left: 264px; }
  .contact.web { left: 542px; }
  .divider { position: absolute; top: 338px; width: 1px; height: 43px; background: var(--ink); }

  .address-band { position: absolute; left: 0; top: 396px; width: 765px; height: 44px; background: var(--orange); }
  .address-band .edge-green { position: absolute; left: 0; top: 0; width: 78px; height: 44px; background: var(--green); }
  .address-band .edge-blue { position: absolute; right: 0; top: 0; width: 81px; height: 44px; background: var(--blue); }
  .address { position: absolute; left: 138px; top: 0; height: 44px; display: flex; align-items: center; gap: 8px; color: var(--white); font-size: 18px; font-weight: 500; white-space: nowrap; }
  .address svg { width: 18px; height: 22px; }
</style>
</head>
<body>
<svg width="0" height="0" style="position:absolute">
  <defs>
    <symbol id="plus-badge" viewBox="0 0 22 22">
      <circle cx="11" cy="11" r="11" fill="#f7931e"/>
      <path d="M11 5.5v11M5.5 11h11" stroke="#fff" stroke-width="2.6" stroke-linecap="round"/>
    </symbol>
    <symbol id="round-badge" viewBox="0 0 38 38">
      <circle cx="19" cy="19" r="18" fill="#4caf62" stroke="#c9e8cf" stroke-width="2"/>
    </symbol>
  </defs>
</svg>

<main class="card">
  <div class="brand-mark"><span class="dot"></span><span class="word">Bright Care</span></div>

  <header class="practice">
    <h1 class="practice-name">Bright Care Partners</h1>
    <p class="practice-tagline">Northfield Spine and Disc</p>
  </header>

  <section class="services">
    <div class="service" style="left:58px;top:15px"><svg><use href="#plus-badge"/></svg>Auto Accident Care</div>
    <div class="service" style="left:290px;top:15px"><svg><use href="#plus-badge"/></svg>Medical Weight loss</div>
    <div class="service" style="left:552px;top:15px"><svg><use href="#plus-badge"/></svg>Chiropractic</div>
    <div class="service" style="left:58px;top:55px"><svg><use href="#plus-badge"/></svg>Primary Care</div>
    <div class="service" style="left:290px;top:55px"><svg><use href="#plus-badge"/></svg>Physical Therapy</div>
  </section>

  <svg class="doctor-tab" viewBox="0 0 765 57">
    <path d="M174 0H570L552 40Q544 57 524 57H220Q200 57 192 40Z" fill="#2e8b4e"/>
  </svg>
  <div class="doctor">
    <svg viewBox="0 0 26 26"><rect x="3" y="3" width="20" height="20" rx="4" fill="none" stroke="#fff" stroke-width="1.6"/><path d="M13 8v10M8 13h10" stroke="#fff" stroke-width="1.8" stroke-linecap="round"/></svg>
    <div>
      <p class="doctor-name">Dr. Tomas Verlinde, D.C.</p>
      <p class="doctor-assoc">Daniel R Mercer, PT, ATC, MS</p>
    </div>
  </div>

  <div class="contact phone">
    <svg viewBox="0 0 38 38"><use href="#round-badge"/><path d="M13 11c1-1 2.5-1 3 0l1.6 3c.4.8 0 1.5-.6 2l-1 .8c1 2 2.6 3.6 4.6 4.6l.8-1c.5-.6 1.2-1 2-.6l3 1.6c1 .5 1 2 0 3-2 2-4.5 2-7.5 0-2.5-1.6-4.4-3.5-6-6-2-3-2-5.5 0-7.4z" fill="#fff"/></svg>
    555.204.7781<br>555.318.6402
  </div>
  <div class="divider" style="left:224px"></div>
  <div class="contact email">
    <svg viewBox="0 0 38 38"><use href="#round-badge"/><rect x="10" y="12.5" width="18" height="13" rx="1.5" fill="#fff"/><path d="M10.5 13.5l8.5 6.5 8.5-6.5" fill="none" stroke="#4caf62" stroke-width="1.5"/></svg>
    info@brightcaredocs.com
  </div>
  <div class="divider" style="left:502px"></div>
  <div class="contact web">
    <svg viewBox="0 0 38 38"><use href="#round-badge"/><g fill="none" stroke="#fff" stroke-width="1.4"><circle cx="19" cy="19" r="9"/><ellipse cx="19" cy="19" rx="4" ry="9"/><path d="M10 19h18M11.5 14h15M11.5 24h15"/></g></svg>
    www.brightcaredocs.com
  </div>

  <footer class="address-band">
    <span class="edge-green"></span>
    <span class="edge-blue"></span>
    <div class="address">
      <svg viewBox="0 0 18 22"><path d="M9 1a7 7 0 0 0-7 7c0 5 7 13 7 13s7-8 7-13a7 7 0 0 0-7-7z" fill="#fff"/><circle cx="9" cy="8" r="2.8" fill="#f7931e"/></svg>
      4820 Ridge Road, Suite 12 | Maple Falls,OR97000
    </div>
  </footer>
</main>
</body>
</html>
```